Upmarket cover for top management book, ideally unlike most common cover pages

This book is about both good management and mismanagement and introduces novel concepts such as the inverse exponential law in strategy, No doubt that these concepts will be criticized by some management scholars. However, students, a few other colleagues and key top managers find the new ideas useful and eye-opening.
The cover must help communicate a deeper vision of management as an expression of life creation and a sort of "divine" energy.

Practical details:
Print and ebook cover page plus elements of the cover for each of the three main book sections.
Title; The Harbor
Subtitle: Field methods and the quiet ripple rule
Author: Teodor M. Vasquel
Publisher: Brightwell Page Press
Width x height: 13,97 x 21,59 cm (without bleed)
Spine: 14-15 cm according to paper color

Target Market(s)

Mostly managers who did not have the opportunity of attending postgraduate management studies such as the MBA

Industry/Entity Type

Mostly high technology

Font styles to use
Serif
Sans Serif
Other font styles liked:
• Arial nova, Arial light

Requirements
Must have
• Preferably cover and back cover on white background, but any good proposals would do.
Nice to have
• An image of bright and reassuring, albeit potentially unlimited, strength. Ideally the cover design should show that good management is good for the COMMON GOOD of society
Should not have
• Please do not show images of people and no proposals reminiscent of other management and strategy book covers

```html
<!DOCTYPE html>
<html lang="en">
<head>
<meta charset="utf-8">
<title>The Harbor — Book Cover</title>
<link rel="stylesheet" href="https://fonts.googleapis.com/css2?family=Bebas+Neue&family=EB+Garamond:ital,wght@1,600;1,700&display=swap">
<style>
  :root {
    --backdrop: #03031a;
    --paper: #ffffff;
    --navy: #07063f;
    --title-blue: #2f5aa6;
    --accent-blue: #2c5fae;
    --band-top: #3057a5;
    --band-bottom: #0a0678;
    --art-deep: #2f58a8;
    --art-mid: #4a8cc6;
    --art-light: #9fd0f0;
  }
  html, body {
    margin: 0;
    width: 1200px;
    height: 1200px;
    overflow: hidden;
    background: var(--backdrop);
  }
  .cover {
    position: absolute;
    left: 242px;
    top: 47px;
    width: 716px;
    height: 1106px;
    background: var(--paper);
    overflow: hidden;
  }
  .title-small {
    position: absolute;
    left: 35px;
    top: 66px;
    margin: 0;
    font-family: "Bebas Neue", "Arial Narrow", sans-serif;
    font-size: 86px;
    line-height: 1;
    color: var(--navy);
  }
  .title-main {
    position: absolute;
    left: 35px;
    top: 148px;
    margin: 0;
    font-family: "Bebas Neue", "Arial Narrow", sans-serif;
    font-weight: 400;
    font-size: 218px;
    line-height: 1;
    letter-spacing: 16px;
    white-space: nowrap;
    background: linear-gradient(to bottom, var(--navy) 18%, var(--title-blue) 38%, var(--navy) 62%);
    -webkit-background-clip: text;
    background-clip: text;
    color: transparent;
  }
  .subtitle {
    position: absolute;
    left: 0;
    width: 716px;
    top: 408px;
    margin: 0;
    text-align: center;
    white-space: nowrap;
    font-family: "EB Garamond", Georgia, serif;
    font-style: italic;
    font-weight: 600;
    font-size: 37px;
    line-height: 1.2;
    color: var(--navy);
  }
  .subtitle .accent {
    font-weight: 700;
    color: var(--accent-blue);
  }
  .artwork {
    position: absolute;
    left: 0;
    top: 555px;
    width: 716px;
    height: 435px;
  }
  .author-band {
    position: absolute;
    left: 0;
    bottom: 0;
    width: 716px;
    height: 116px;
    background: linear-gradient(to bottom, var(--band-top), var(--band-bottom));
    display: flex;
    align-items: center;
    justify-content: center;
  }
  .author {
    margin: 0;
    font-family: "Bebas Neue", "Arial Narrow", sans-serif;
    font-size: 54px;
    letter-spacing: 14px;
    color: var(--paper);
    padding-left: 14px;
  }
</style>
</head>
<body>
  <main class="cover">
    <p class="title-small">The</p>
    <h1 class="title-main">HARBOR</h1>
    <p class="subtitle"><span class="accent">Field</span> methods and the quiet ripple rule</p>

    <svg class="artwork" viewBox="0 0 716 435" role="img" aria-label="Illustration area: blue silhouettes of a group of business people facing a single standing figure, with light reflections on a glossy floor">
      <defs>
        <linearGradient id="art-fade" x1="0" y1="0" x2="0" y2="1">
          <stop offset="0" stop-color="#ffffff"/>
          <stop offset="0.35" stop-color="var(--art-mid)" stop-opacity="0.35"/>
          <stop offset="0.7" stop-color="var(--art-deep)" stop-opacity="0.55"/>
          <stop offset="1" stop-color="var(--art-light)" stop-opacity="0.6"/>
        </linearGradient>
        <linearGradient id="art-side" x1="0" y1="0" x2="1" y2="0">
          <stop offset="0" stop-color="#ffffff" stop-opacity="0"/>
          <stop offset="0.6" stop-color="#ffffff" stop-opacity="0.55"/>
          <stop offset="1" stop-color="#ffffff" stop-opacity="0.3"/>
        </linearGradient>
      </defs>
      <rect width="716" height="435" fill="url(#art-fade)"/>
      <rect width="716" height="435" fill="url(#art-side)"/>
    </svg>

    <footer class="author-band">
      <p class="author">Teodor M. Vasquel</p>
    </footer>
  </main>
</body>
</html>
```